CLS Business card, letterhead, and stationery, email tag, fax cover
Clear and Professional material
Simple
Léandre Ormessac
Directeur des ventes
47, rue de Valmorin
Paris , 75016
France
leandre@clsys.fr
www.clsys.fr
Logo + tag line
LOGO
SMALL LOGO

```html
<!DOCTYPE html>
<html lang="fr">
<head>
<meta charset="utf-8">
<title>Corvane Lumis Systems — cartes de visite</title>
<link rel="stylesheet" href="https://fonts.googleapis.com/css2?family=Open+Sans:wght@400;600;700&family=Tinos:ital,wght@0,400;1,400&display=swap">
<style>
  :root {
    --backdrop: #e9e6e2;
    --card: #ffffff;
    --brand-blue: #1ba6d8;
    --brand-grey: #5d6670;
    --ink: #2b2b2b;
    --divider: #c9ccd0;
  }
  * { box-sizing: border-box; margin: 0; padding: 0; }
  html, body { width: 1200px; height: 852px; overflow: hidden; }
  body {
    background: var(--backdrop);
    position: relative;
    font-family: "Tinos", "Times New Roman", serif;
    color: var(--ink);
  }
  .icon-defs { position: absolute; width: 0; height: 0; }

  .card {
    position: absolute;
    width: 620px;
    height: 360px;
    background: var(--card);
    border-radius: 22px;
    box-shadow: 0 6px 18px rgba(0,0,0,0.12);
  }
  .card--horizontal { left: 60px; top: 56px; }
  .card--stacked { left: 520px; top: 436px; }

  .brand {
    position: absolute;
    display: flex;
    flex-direction: column;
    align-items: flex-start;
    font-family: "Open Sans", Arial, sans-serif;
    color: var(--brand-blue);
  }
  .brand__row { display: flex; align-items: center; gap: 10px; }
  .brand__dot {
    width: 14px; height: 14px; border-radius: 50%;
    background: var(--brand-blue);
    flex: none;
  }
  .brand__name {
    font-weight: 600;
    font-size: 27px;
    line-height: 1.1;
  }
  .brand__tagline {
    font-weight: 600;
    font-size: 14px;
    margin-top: 8px;
    margin-left: 24px;
  }

  .divider { position: absolute; background: var(--divider); }

  .holder__name {
    font-family: "Open Sans", Arial, sans-serif;
    font-weight: 700;
    font-size: 22px;
    color: var(--brand-blue);
  }
  .holder__role {
    font-style: italic;
    font-size: 16px;
    color: var(--brand-grey);
    margin-top: 2px;
  }
  .address {
    font-size: 17px;
    line-height: 1.3;
    margin-top: 16px;
  }
  .contacts { list-style: none; font-size: 17px; }
  .contacts li {
    display: flex;
    align-items: center;
    gap: 12px;
    height: 27px;
  }
  .contacts svg { width: 15px; height: 15px; fill: var(--brand-blue); flex: none; }

  /* horizontal card */
  .card--horizontal .brand { left: 40px; top: 138px; }
  .card--horizontal .divider { left: 305px; top: 34px; width: 1px; height: 180px; }
  .card--horizontal .holder { position: absolute; left: 325px; top: 30px; }
  .card--horizontal .contacts { position: absolute; left: 325px; top: 190px; }

  /* stacked card */
  .card--stacked .brand { left: 200px; top: 46px; }
  .card--stacked .holder {
    position: absolute; right: 330px; top: 170px; text-align: right;
  }
  .card--stacked .divider { left: 305px; top: 172px; width: 1px; height: 150px; }
  .card--stacked .contacts { position: absolute; left: 325px; top: 168px; }
</style>
</head>
<body>

<svg class="icon-defs" aria-hidden="true">
  <symbol id="icon-phone" viewBox="0 0 16 16">
    <path d="M3.6 1.2l2.3 2.6-1.3 1.8c.9 2 2.6 3.7 4.6 4.6l1.8-1.3 2.6 2.3-1.4 2.3C7 13.3 2.7 9 2.5 3z"/>
  </symbol>
  <symbol id="icon-mobile" viewBox="0 0 16 16">
    <path d="M4.5 0.5h7a1 1 0 0 1 1 1v13a1 1 0 0 1-1 1h-7a1 1 0 0 1-1-1v-13a1 1 0 0 1 1-1zm.6 2v9.5h5.8V2.5zM8 12.8a.9.9 0 1 0 0 1.8.9.9 0 0 0 0-1.8z"/>
  </symbol>
  <symbol id="icon-fax" viewBox="0 0 16 16">
    <path d="M4 1h6l2 2v3H4zM2 7h12a1 1 0 0 1 1 1v5a1 1 0 0 1-1 1H2a1 1 0 0 1-1-1V8a1 1 0 0 1 1-1zm2 2v1.5h2V9zm3.5 0v1.5h2V9zM4 11.5V13h2v-1.5zm3.5 0V13h2v-1.5z"/>
  </symbol>
  <symbol id="icon-mail" viewBox="0 0 16 16">
    <path d="M8 1a7 7 0 1 0 3.4 13.1l-.6-1.2A5.6 5.6 0 1 1 13.6 8v.8c0 .8-.5 1.3-1.1 1.3s-1.1-.5-1.1-1.3V4.6h-1.3v.6A3.3 3.3 0 1 0 10.5 10a2.4 2.4 0 0 0 2 1.2c1.5 0 2.5-1.1 2.5-2.7V8A7 7 0 0 0 8 1zm0 4.9a2.1 2.1 0 1 1 0 4.2 2.1 2.1 0 0 1 0-4.2z"/>
  </symbol>
  <symbol id="icon-web" viewBox="0 0 16 16">
    <path d="M8 1a7 7 0 1 0 0 14A7 7 0 0 0 8 1zm4.8 6.2h-2.1a11 11 0 0 0-.9-4.1 5.6 5.6 0 0 1 3 4.1zM8 2.6c.6.8 1.2 2.5 1.3 4.6H6.7C6.8 5.1 7.4 3.4 8 2.6zM6.2 3.1a11 11 0 0 0-.9 4.1H3.2a5.6 5.6 0 0 1 3-4.1zM3.2 8.8h2.1a11 11 0 0 0 .9 4.1 5.6 5.6 0 0 1-3-4.1zM8 13.4c-.6-.8-1.2-2.5-1.3-4.6h2.6c-.1 2.1-.7 3.8-1.3 4.6zm1.8-.5a11 11 0 0 0 .9-4.1h2.1a5.6 5.6 0 0 1-3 4.1z"/>
  </symbol>
</svg>

<section class="card card--horizontal" aria-label="Carte de visite, version horizontale">
  <div class="brand">
    <div class="brand__row">
      <span class="brand__dot"></span>
      <span class="brand__name">Corvane Lumis<br>Systems</span>
    </div>
    <span class="brand__tagline">solutions avancées de la peau</span>
  </div>

  <div class="divider"></div>

  <div class="holder">
    <p class="holder__name">Léandre Ormessac</p>
    <p class="holder__role">Directeur des ventes</p>
    <p class="address">47, rue de Valmorin<br>Paris , 75016<br>France</p>
  </div>

  <ul class="contacts">
    <li><svg><use href="#icon-phone"/></svg>01.45.17.60.32</li>
    <li><svg><use href="#icon-mobile"/></svg>06.58.41.27.93</li>
    <li><svg><use href="#icon-fax"/></svg>01.45.17.60.33</li>
    <li><svg><use href="#icon-mail"/></svg>leandre@clsys.fr</li>
    <li><svg><use href="#icon-web"/></svg>www.clsys.fr</li>
  </ul>
</section>

<section class="card card--stacked" aria-label="Carte de visite, version empilée">
  <div class="brand">
    <div class="brand__row">
      <span class="brand__dot"></span>
      <span class="brand__name">Corvane Lumis<br>Systems</span>
    </div>
    <span class="brand__tagline">solutions avancées de la peau</span>
  </div>

  <div class="holder">
    <p class="holder__name">Léandre Ormessac</p>
    <p class="holder__role">Directeur des ventes</p>
    <p class="address">47, rue de Valmorin<br>Paris , 75016<br>France</p>
  </div>

  <div class="divider"></div>

  <ul class="contacts">
    <li><svg><use href="#icon-phone"/></svg>01.45.17.60.32</li>
    <li><svg><use href="#icon-mobile"/></svg>06.58.41.27.93</li>
    <li><svg><use href="#icon-fax"/></svg>01.45.17.60.33</li>
    <li><svg><use href="#icon-mail"/></svg>leandre@clsys.fr</li>
    <li><svg><use href="#icon-web"/></svg>www.clsys.fr</li>
  </ul>
</section>

</body>
</html>
```